wardrobe/costume stylist needs good business card for own business

Hi:)

I'm wanting a business card for my company. I am a freelance stylist.

I do wardrobe/costume stylist to TV commercials; Films; Fashion and Lifestyle shoots.

I'd like a design based around my name Rosalind Pember written nicely, maybe a colour? Up to you?!

I've attached a couple of images of business cards I like
.... be creative and have fun!

Thank you :)
Updates

Reason: I was trying to get my new business card ready for before I headed overseas Friday morning but I don't think that was realistic so I'd like to extend the deadline to give time to the project. Thank you

Hi designers:) Thank you for all your designs, I've extended the deadline until Sunday, so there's a bit more time. I've attached 3 pictures of business cards which I quite like, please take a look to see if it can be of help in your process. I like the pale plain or patterned background with dark font and the dark plain or patterned background with the pale font the motifs the feminine fonts the plain fonts I like the idea of playing with a circle or some shape on one side of the card with my name or initials as in the picture I have on my post could you play around with this idea a bit please? Thank you all for the work you've done :) Rosa

Hi I am working overseas til Saturday night sorry for no feedback until I teturn Thanks :) Rosa

Hi designers, Thank you all so much for submitting your designs, I really appreciate your input into my project :) I'm sorry I didn't get to respond to some comments, and give feedback. I didn't back from being away until later than I expected, and the deadline had passed then, so apologies. Thanks to you all again for all your really good designs :) Rosa

Target Market(s)

I am a freelance stylist my target audience is producers, production companies, photographers, directors...

Industry/Entity Type

Business

Requirements
Must have
• Rosalind Pember
Stylist or Wardrobe Stylist

email rosapember@quillnet.co.nz
Mobile 0218846193

(Don't have to use the words 'email' and 'mobile')
Nice to have
• Would like it to be double sided
Like B & W
Like pale colour background with dark font or white font
Like dark colour background with pale font
Should not have
• I would prefer it not to incorporate pictures

```html
<!DOCTYPE html>
<html lang="en">
<head>
<meta charset="utf-8">
<title>Rosalind Pember — Wardrobe Stylist Business Card</title>
<link rel="stylesheet" href="https://fonts.googleapis.com/css2?family=Andada+Pro:wght@400;600;700&display=swap">
<style>
  :root {
    --backdrop: #d9d3c5;
    --olive-deep: #3b4220;
    --olive-light: #5d6738;
    --cream: #eef2c2;
    --cream-shade: #e2e8b0;
    --ink: #3b4220;
  }
  * { box-sizing: border-box; margin: 0; padding: 0; }
  html, body {
    width: 1200px;
    height: 900px;
    overflow: hidden;
  }
  body {
    position: relative;
    background: var(--backdrop);
    font-family: "Andada Pro", Georgia, serif;
  }
  .card {
    position: absolute;
    width: 640px;
    height: 366px;
    border-radius: 18px;
    box-shadow: 0 10px 26px rgba(40, 34, 20, 0.28);
    overflow: hidden;
  }
  /* Reverse side */
  .card--back {
    left: 170px;
    top: 48px;
    background: linear-gradient(90deg, var(--olive-deep) 0%, var(--olive-deep) 35%, var(--olive-light) 100%);
  }
  .back-emblem {
    position: absolute;
    left: 50%;
    top: 50%;
    width: 168px;
    height: 168px;
    margin: -84px 0 0 -84px;
    border-radius: 50%;
    background: var(--cream);
    display: flex;
    align-items: center;
    justify-content: center;
    text-align: center;
  }
  .back-emblem__name {
    color: var(--ink);
    font-weight: 600;
    font-size: 24px;
    line-height: 1.15;
  }
  /* Front side */
  .card--front {
    left: 390px;
    top: 486px;
    background: linear-gradient(100deg, var(--cream-shade) 0%, var(--cream) 60%, #f3f6d2 100%);
    color: var(--ink);
  }
  .name-block {
    position: absolute;
    left: 64px;
    top: 34px;
    width: 222px;
    height: 200px;
    background: var(--olive-deep);
  }
  .name-first {
    position: absolute;
    left: 82px;
    top: 150px;
    font-size: 46px;
    font-weight: 600;
    color: var(--cream);
    line-height: 1;
  }
  .name-last {
    position: absolute;
    left: 292px;
    top: 146px;
    font-size: 54px;
    font-weight: 700;
    color: var(--ink);
    line-height: 1;
    letter-spacing: 0.5px;
  }
  .role {
    position: absolute;
    left: 294px;
    top: 206px;
    font-size: 19px;
    font-weight: 600;
    letter-spacing: 3px;
    color: var(--ink);
  }
  .contact {
    position: absolute;
    left: 64px;
    bottom: 58px;
    font-size: 21px;
    color: var(--ink);
    letter-spacing: 0.5px;
  }
  .contact__divider { margin: 0 10px; }
</style>
</head>
<body>
  <section class="card card--back" aria-label="Card reverse">
    <div class="back-emblem">
      <span class="back-emblem__name">Rosalind<br>Pember</span>
    </div>
  </section>

  <section class="card card--front" aria-label="Card front">
    <div class="name-block"></div>
    <span class="name-first">Rosalind</span>
    <span class="name-last">pember</span>
    <span class="role">wardrobe stylist</span>
    <p class="contact">
      <span class="contact__phone">0218846193</span><span class="contact__divider">|</span><span class="contact__email">rosapember@quillnet.co.nz</span>
    </p>
  </section>
</body>
</html>
```